We have a menu to be designed with an "old school" diner theme. There will be a total of 10 pages including a full color cover.
Looking for several "looks" to present the owner, so if you have a few ideas for concepts...please include them. Need at least the cover and 1-3 interior pages to present before completing the entire 10 pages.
We would like to have the concepts available to present on Tuesday August 27th if possible.
Once a concept is chosen, we will need all 10 pages setup and ready to print. We will need the final design sent to us in an editable file (InDesign is preferred).
Size: 8.5" wide by 14" high
Color: Full color with 1/8" bleeds
We are providing the current menu for text of menu items only...not for layout.
Please do NOT use leaders ( ..............4.99) in front of prices and do NOT use dollar sign symbols ($). Please insert the prices at the end of each description with 2 spaces before the price. See below for an example:
____________________________________
Tuna
Freshly made tuna mixed with celery
and Brackley’s mayo (no onion) and
with lettuce 7.29
Please use an easily legible font for the descriptions and something a little more bold for the item names.
Please follow the order of the items as they are on the attached PDF.
You can see what they currently have on their website:
http://www.copperkettlegrill.example/
Updates
My apologies for not getting that PDF and logo uploaded. I thought it had been submitted.
They are both uploaded now.
Thanks!
Really need to try to get the concepts in asap to show our client. Thanks!
Thank you all for submitting the designs. We would like to see some different looks for the inside pages. Lots of covers have been submitted, but not very many inside pages. Please send a sample or two as soon as possible. We would like to choose a design soon.
Thank you!
Diner

```html
<!DOCTYPE html>
<html lang="en">
<head>
<meta charset="utf-8">
<title>Copper Kettle Grill – Menu</title>
<link href="https://fonts.googleapis.com/css2?family=Questrial&family=Pinyon+Script&family=Playball&family=Cinzel:wght@700&display=swap" rel="stylesheet">
<style>
  :root{
    --stage:#ece7df;
    --wood-light:#ddd2c2;
    --wood-mid:#cfc2ae;
    --maroon:#5e1a22;
    --maroon-band:#7b2a31;
    --wine:#9a2a34;
    --ink:#1f1a17;
    --paper:#f7f4ef;
    --cream:#f1ead6;
    --frame:#6b4a40;
    --band:#7d6d64;
    --white:#ffffff;
  }
  *{box-sizing:border-box;margin:0;padding:0}
  html,body{width:1200px;height:1050px;overflow:hidden;background:var(--stage)}
  .spread{
    position:absolute;left:18px;top:46px;width:970px;height:798px;
    transform:scale(1.2);transform-origin:0 0;
    font-family:"Questrial",sans-serif;color:var(--ink);
    box-shadow:0 2px 8px rgba(0,0,0,.18);
  }
  .panel{position:absolute;top:0;height:798px;width:485px;
    background:linear-gradient(90deg,var(--wood-light),#e4dacb 30%,var(--wood-mid) 55%,#e1d6c6 80%,var(--wood-light))}
  .panel--back{left:0;border-right:1px solid rgba(0,0,0,.08)}
  .panel--front{left:485px}

  .menu-box{position:absolute;background:var(--paper);border:1px solid #4a3a36}
  .menu-box__title{height:36px;background:var(--maroon);color:var(--white);
    font-family:"Pinyon Script",cursive;font-size:24px;text-align:center;line-height:38px;
    border-bottom:2px solid #c9b9a9}
  .photo{position:absolute}
  .col{position:absolute;list-style:none;font-size:10px}
  .col li{display:flex;justify-content:space-between}
  .side-orders .col li{height:20px}
  .desserts .col li{height:20px}
  .beverages .col li{height:14px}
  .note{position:absolute;font-size:10px;white-space:nowrap}
  .note span{margin-left:12px}

  .side-orders{left:30px;top:61px;width:426px;height:153px}
  .desserts{left:90px;top:296px;width:296px;height:126px}
  .beverages{left:30px;top:504px;width:426px;height:152px}

  .contact-bar{position:absolute;left:0;top:716px;width:485px;height:82px;
    background:var(--maroon-band);border-top:2px solid #b0646a;color:var(--white)}
  .brand-mark{position:absolute;left:18px;top:18px;width:92px;display:flex;flex-direction:column;align-items:center;gap:4px}
  .brand-mark__dot{width:28px;height:28px;border-radius:50%;background:#f0c43a}
  .brand-mark__name{font-size:10px;text-align:center;line-height:1.1;color:var(--white)}
  .follow{position:absolute;left:133px;top:10px;font-size:12.5px}
  .social{position:absolute;left:133px;top:30px;display:flex;gap:18px}
  .social span{width:36px;height:36px;border-radius:50%;background:#e9e4dd;border:2px solid #fff}
  .address{position:absolute;left:304px;top:12px;font-size:12px;line-height:15px}

  .tagline-top{position:absolute;left:0;right:0;top:38px;text-align:center;font-size:21px}
  .ribbon-band{position:absolute;left:0;width:485px;top:276px;height:118px}
  .emblem{position:absolute;left:100px;top:128px;width:300px;height:410px;
    background:var(--cream);border:6px solid var(--frame);border-radius:60px 60px 40px 40px;
    box-shadow:0 3px 6px rgba(0,0,0,.25)}
  .emblem__name{position:absolute;left:0;right:0;top:74px;text-align:center;
    font-family:"Playball",cursive;font-size:31px;line-height:40px;color:var(--wine)}
  .cutlery{position:absolute;left:150px;top:303px;width:195px;height:180px;
    background:radial-gradient(ellipse at center,#8a6a5e 0%,#b59a8c 45%,rgba(241,234,214,0) 75%)}
  .ribbon{position:absolute;left:100px;top:448px;width:297px;height:105px}
  .family{position:absolute;left:0;right:0;top:616px;text-align:center;font-size:24px}
  .slogan{position:absolute;left:0;right:0;top:700px;text-align:center;
    font-family:"Pinyon Script",cursive;font-size:33px;line-height:45px;color:#6e1e26}
</style>
</head>
<body>
<main class="spread">
  <section class="panel panel--back">
    <article class="menu-box side-orders">
      <h2 class="menu-box__title">Side Orders</h2>
      <div class="photo" role="img" aria-label="Photo of French fries in a white tray" style="left:6px;top:45px;width:142px;height:97px;background:radial-gradient(ellipse at center,#e8b04a 0%,#f3d68a 45%,#fbf7ee 80%)"></div>
      <ul class="col" style="left:158px;top:51px;width:120px">
        <li><span>French fries</span><span>1.95</span></li>
        <li><span>Scoop of cottage</span><span>1.40</span></li>
        <li><span>Side of tomatoes</span><span>1.00</span></li>
        <li><span>Vegetable of the day</span><span>1.40</span></li>
        <li><span>Rice Pilaf</span><span>1.40</span></li>
      </ul>
      <ul class="col" style="left:294px;top:51px;width:124px">
        <li><span>Cole slaw</span><span>1.40</span></li>
        <li><span>Potato salad</span><span>1.40</span></li>
        <li><span>Onion rings</span><span>2.50</span></li>
        <li><span>Fresh fruit cup</span><span>3.95</span></li>
        <li><span>Mashed potato</span><span>1.70</span></li>
      </ul>
    </article>

    <article class="menu-box desserts">
      <h2 class="menu-box__title">Homemade Desserts</h2>
      <div class="photo" role="img" aria-label="Photo of a slice of key lime pie" style="left:11px;top:47px;width:112px;height:75px;background:linear-gradient(135deg,#c9a040,#e8dca0 45%,#3a8a6a 75%,#c24a3a)"></div>
      <ul class="col" style="left:135px;top:56px;width:140px">
        <li><span>Key Lime Pie</span><span>3.00</span></li>
        <li><span>Rice Pudding</span><span>3.00</span></li>
        <li><span>Dessert of the Day</span><span>3.00</span></li>
      </ul>
    </article>

    <article class="menu-box beverages">
      <h2 class="menu-box__title">Beverages</h2>
      <div class="photo" role="img" aria-label="Photo of iced tea with lemon and mint" style="left:6px;top:45px;width:79px;height:101px;background:linear-gradient(160deg,#e58a2a,#f2b24a 45%,#9bc25a 80%)"></div>
      <ul class="col" style="left:94px;top:50px;width:146px">
        <li><span>Coffee or Ice Coffee</span><span>1.75</span></li>
        <li><span>Hot Tea(regular or Decaf)</span><span>1.75</span></li>
        <li><span>Ice Tea or Sweet Tea</span><span>1.95</span></li>
        <li><span>Fountain Sodas</span><span>1.95</span></li>
      </ul>
      <ul class="col" style="left:261px;top:50px;width:147px">
        <li><span>Summit Iced Tea</span><span>1.85</span></li>
        <li><span>Old Mill Soda</span><span>1.85</span></li>
        <li><span>Lemonade</span><span>1.95</span></li>
      </ul>
      <p class="note" style="left:140px;top:118px">Chocolate Milk med <span>1.95</span><span>lg</span><span>2.50</span></p>
      <p class="note" style="left:140px;top:132px">Hot chocolate with whipped Cream <span style="margin-left:4px">2.50</span></p>
    </article>

    <footer class="contact-bar">
      <div class="brand-mark">
        <span class="brand-mark__dot"></span>
        <span class="brand-mark__name">Copper Kettle Grill</span>
      </div>
      <p class="follow">Follow Copper Kettle Grill</p>
      <div class="social" aria-label="Social links"><span></span><span></span><span></span></div>
      <p class="address">www.copperkettlegrill.example<br>W. Harbor Ave Millbrook<br>FL 30000 (555) 014-2985</p>
    </footer>
  </section>

  <section class="panel panel--front">
    <p class="tagline-top">Home-Style Cooking Est. 1989</p>
    <svg class="ribbon-band" viewBox="0 0 485 118" aria-hidden="true">
      <rect x="0" y="0" width="485" height="118" fill="#eee6da" opacity=".7"/>
      <rect x="0" y="24" width="485" height="72" fill="var(--band)"/>
      <line x1="0" y1="27" x2="485" y2="27" stroke="#a39489" stroke-width="1"/>
      <line x1="0" y1="93" x2="485" y2="93" stroke="#a39489" stroke-width="1"/>
    </svg>
    <div class="emblem">
      <h1 class="emblem__name">Copper Kettle<br>Grill</h1>
    </div>
    <div class="cutlery" role="img" aria-label="Illustration of a spoon, fork and knife"></div>
    <svg class="ribbon" viewBox="0 0 297 105">
      <polygon points="0,70 40,62 30,82 48,100 8,104" fill="#7a1f28"/>
      <polygon points="297,30 257,28 268,48 250,64 290,70" fill="#7a1f28"/>
      <path d="M30,62 Q150,20 270,30 L265,70 Q150,58 40,100 Z" fill="var(--wine)"/>
      <text x="150" y="70" text-anchor="middle" font-family="Cinzel, serif" font-weight="700" font-size="26" letter-spacing="5" fill="#fff" transform="rotate(-8 150 62)">MENU</text>
    </svg>
    <p class="family">Family-Friendly Restaurant</p>
    <p class="slogan">Where good friends meet<br>and the food is hard to beat!</p>
  </section>
</main>
</body>
</html>
```